Recipe Card Design

I have a small kitchen store in Livingston Montana, and I would like to have recipe cards (4x6 postcard) designed with my logo, lines for recipe writing, all in black and white. My website is here: www.brambleforkpantry.com

Store

```html
<!DOCTYPE html>
<html lang="en">
<head>
<meta charset="utf-8">
<title>Recipe Card – Bramble Fork Pantry</title>
<link rel="stylesheet" href="https://fonts.googleapis.com/css2?family=Amatic+SC:wght@700&family=Josefin+Slab:wght@600&family=Kaushan+Script&display=swap">
<style>
  :root {
    --ink: #111111;
    --paper: #ffffff;
    --rule: #333333;
  }
  * { margin: 0; padding: 0; box-sizing: border-box; }
  html, body {
    width: 1200px;
    height: 930px;
    overflow: hidden;
    background: var(--paper);
  }
  .card {
    position: relative;
    width: 1200px;
    height: 930px;
    background: var(--paper);
    color: var(--ink);
  }
  .card-frame {
    position: absolute;
    inset: 0;
  }

  /* Front side: slogan */
  .slogan-main {
    position: absolute;
    left: 88px;
    top: 200px;
    font-family: "Kaushan Script", cursive;
    font-weight: 400;
    font-size: 162px;
    line-height: 1;
    letter-spacing: 8px;
    white-space: nowrap;
  }
  .slogan-outside {
    position: absolute;
    left: 222px;
    top: 382px;
    font-family: "Josefin Slab", serif;
    font-weight: 600;
    font-size: 62px;
    line-height: 1;
    letter-spacing: 2px;
  }
  .slogan-bridge {
    position: absolute;
    left: 116px;
    top: 450px;
    font-family: "Kaushan Script", cursive;
    font-size: 34px;
    line-height: 1;
    white-space: nowrap;
  }
  .slogan-inside {
    position: absolute;
    left: 340px;
    top: 440px;
    font-family: "Josefin Slab", serif;
    font-weight: 600;
    font-size: 62px;
    line-height: 1;
    letter-spacing: 2px;
  }
  .site-link {
    position: absolute;
    left: 93px;
    top: 752px;
    font-family: "Amatic SC", sans-serif;
    font-weight: 700;
    line-height: 1.05;
    letter-spacing: 1.5px;
  }
  .site-link .label { display: block; font-size: 27px; }
  .site-link .url { display: block; font-size: 33px; }

  /* Back side: brand + writing lines */
  .brand {
    position: absolute;
    left: 868px;
    top: 140px;
    width: 210px;
    display: flex;
    align-items: center;
    gap: 10px;
    font-family: "Amatic SC", sans-serif;
    font-weight: 700;
    font-size: 40px;
    line-height: 1;
  }
  .brand-square {
    flex: none;
    width: 22px;
    height: 22px;
    background: var(--ink);
  }
  .field-label {
    position: absolute;
    font-family: "Amatic SC", sans-serif;
    font-weight: 700;
    font-size: 32px;
    line-height: 1;
    letter-spacing: 1.5px;
  }
  .field-recipe { left: 748px; top: 325px; }
  .field-ingredients { left: 748px; top: 379px; }
  .field-instructions { left: 748px; top: 522px; }
</style>
</head>
<body>
<main class="card">
  <svg class="card-frame" width="1200" height="930" viewBox="0 0 1200 930" aria-hidden="true">
    <path d="M110,30 H1090 A80,80 0 0 0 1170,110 V820 A80,80 0 0 0 1090,900 H110 A80,80 0 0 0 30,820 V110 A80,80 0 0 0 110,30 Z"
          fill="none" stroke="var(--ink)" stroke-width="6"/>
    <g fill="var(--ink)">
      <ellipse cx="60" cy="52" rx="30" ry="22"/>
      <ellipse cx="1140" cy="52" rx="30" ry="22"/>
      <ellipse cx="60" cy="878" rx="30" ry="22"/>
      <ellipse cx="1140" cy="878" rx="30" ry="22"/>
    </g>
    <g stroke="var(--ink)" stroke-width="4">
      <line x1="53" y1="118" x2="53" y2="812"/>
      <line x1="1148" y1="118" x2="1148" y2="812"/>
    </g>
    <line class="divider" x1="717" y1="73" x2="717" y2="862" stroke="var(--rule)" stroke-width="1.5"/>
    <g class="writing-lines" stroke="var(--rule)" stroke-width="1.2">
      <line x1="847" y1="350" x2="1148" y2="350"/>
      <line x1="900" y1="406" x2="1148" y2="406"/>
      <line x1="749" y1="458" x2="1148" y2="458"/>
      <line x1="751" y1="506" x2="1148" y2="506"/>
      <line x1="924" y1="551" x2="1153" y2="551"/>
      <line x1="744" y1="600" x2="1148" y2="600"/>
      <line x1="740" y1="656" x2="1148" y2="656"/>
      <line x1="739" y1="703" x2="1148" y2="703"/>
      <line x1="749" y1="756" x2="1148" y2="756"/>
      <line x1="749" y1="803" x2="1148" y2="803"/>
    </g>
  </svg>

  <h1 class="slogan-main">Healthy</h1>
  <p class="slogan-outside">OUTSIDE</p>
  <p class="slogan-bridge">starts from the</p>
  <p class="slogan-inside">INSIDE</p>

  <p class="site-link">
    <span class="label">Visit for more:</span>
    <span class="url">www.brambleforkpantry.com</span>
  </p>

  <div class="brand">
    <span class="brand-square"></span>
    <span class="brand-name">Bramble Fork Pantry</span>
  </div>

  <p class="field-label field-recipe">Receipe:</p>
  <p class="field-label field-ingredients">Ingredients:</p>
  <p class="field-label field-instructions">Instructions:</p>
</main>
</body>
</html>
```